Volunteer fire fighters needed banner

As part of our recruitment campaign, we need a sign we can post on our sign trailer to entice locals to join our volunteer fire service. This design will be printed on a banner, front and back, to catch traffic going in both directions on a busy roadway. This banner will have a printed surface of 4 feet tall by 8 feet long.
Our fire department is looking to attract people between the ages of 18 and 35 years old who are interested in being a firefighter. We offer our volunteers:
-Free professional training
-All equipment supplied
-Tax abatements for active volunteers
For more information, you can check us out at:
Brookmerecrestfire.example

This design should:
-scale to and fit a 4'x8' canvas
-Include our web address "BrookmereCrestFire.example"
-Say "Members Wanted"
-"Drill every Tuesday at 7pm"
-"37 Quarry Bend Lane"
-Include "Brookmere Crest Fire Department"

We've included reference photos and past images we use for our other campaigns for inspiration for you.

Target Market(s)

18-35 y/o

Industry/Entity Type

Fire Service

Requirements
Must have
• -scale to and fit a 4'x8' canvas -Include our web address "BrookmereCrestFire.example" -Say "Members Wanted" -"Drill every Tuesday at 7pm" -"37 Quarry Bend Lane" -Include "Brookmere Crest Fire Department"

```html
<!DOCTYPE html>
<html lang="en">
<head>
<meta charset="utf-8">
<title>Brookmere Crest Fire Department – Recruitment Banner</title>
<link rel="stylesheet" href="https://fonts.googleapis.com/css2?family=Alfa+Slab+One&family=Montserrat:wght@500;600;700&display=swap">
<style>
  :root {
    --red: #d2202a;
    --red-dark: #9e1218;
    --navy: #26307a;
    --navy-deep: #1a2260;
    --white: #ffffff;
    --panel: rgba(214, 214, 232, 0.82);
    --stage: #e9ecf2;
  }
  * { box-sizing: border-box; margin: 0; padding: 0; }
  html, body { width: 1200px; height: 800px; overflow: hidden; background: var(--stage); }
  .banner {
    position: absolute; left: 0; top: 100px; width: 1200px; height: 600px;
    background: radial-gradient(ellipse at 60% 45%, var(--navy) 0%, var(--navy-deep) 100%);
    font-family: "Montserrat", sans-serif; color: var(--white); overflow: hidden;
  }
  .headline-band {
    position: absolute; left: 0; top: 0; width: 100%; height: 112px;
    background: linear-gradient(180deg, #e23038 0%, var(--red) 55%, var(--red-dark) 100%);
    display: flex; align-items: center; padding-left: 48px;
  }
  .headline {
    font-family: "Alfa Slab One", serif; font-weight: 400; font-size: 74px;
    letter-spacing: 2px; text-transform: uppercase; line-height: 1;
  }
  .dept-mark {
    position: absolute; right: 40px; top: 130px; display: flex; align-items: center; gap: 10px;
    font-weight: 700; font-size: 20px; color: var(--white);
  }
  .dept-mark .dot { width: 26px; height: 26px; border-radius: 50%; background: var(--red); }
  .dept-name {
    position: absolute; left: 40px; top: 172px;
    font-family: "Alfa Slab One", serif; font-weight: 400; font-size: 32px;
    letter-spacing: 1px; text-transform: uppercase; line-height: 1;
  }
  .photos { position: absolute; left: 40px; top: 232px; display: flex; gap: 26px; }
  .photo { width: 160px; height: 282px; border: 3px solid rgba(255,255,255,0.15); }
  .photo--responder { background: linear-gradient(160deg, #8a6b5a, #3d3a44); }
  .photo--engine { background: linear-gradient(160deg, #c8323a, #5e4a42); }
  .photo--gear { background: linear-gradient(160deg, #5d6c8c, #7a5a45); }
  .offer { position: absolute; left: 600px; top: 232px; width: 562px; }
  .offer-title {
    background: var(--red); padding: 14px 24px;
    font-weight: 700; font-size: 24px; text-transform: uppercase; letter-spacing: 1px;
  }
  .offer-list {
    list-style: none; background: var(--panel); padding: 20px 24px; color: var(--white);
    border-radius: 0 0 10px 10px;
  }
  .offer-list li {
    font-weight: 600; font-size: 18px; text-transform: uppercase; letter-spacing: 0.5px;
    display: flex; align-items: center; gap: 14px; line-height: 1.8;
    text-shadow: 0 1px 2px rgba(20,25,80,0.5);
  }
  .offer-list li::before {
    content: ""; width: 11px; height: 11px; border-radius: 50%; background: var(--red); flex: none;
  }
  .more-info {
    position: absolute; left: 600px; top: 470px; width: 562px;
    font-weight: 600; font-size: 14px; text-transform: uppercase; letter-spacing: 0.5px;
  }
  .web {
    display: block; margin-top: 8px; font-weight: 500; font-size: 28px;
    text-align: right; letter-spacing: 1px; text-transform: none;
  }
  .footer-band {
    position: absolute; left: 0; bottom: 0; width: 100%; height: 58px;
    background: linear-gradient(180deg, var(--red) 0%, var(--red-dark) 100%);
    display: flex; align-items: center; gap: 28px; padding-left: 40px;
    font-weight: 500; font-size: 25px; letter-spacing: 0.5px;
  }
  .footer-band .sep { width: 9px; height: 9px; border-radius: 50%; background: var(--white); }
</style>
</head>
<body>
  <main class="banner">
    <header class="headline-band">
      <h1 class="headline">Members Wanted</h1>
    </header>
    <div class="dept-mark"><span class="dot"></span>Brookmere Crest</div>
    <h2 class="dept-name">Brookmere Crest Fire Department</h2>

    <section class="photos">
      <div class="photo photo--responder" role="img" aria-label="Photo of a volunteer firefighter in turnout gear carrying a medical bag"></div>
      <div class="photo photo--engine" role="img" aria-label="Photo of the front of a red fire engine in the station bay"></div>
      <div class="photo photo--gear" role="img" aria-label="Photo of a firefighter in full gear with helmet and breathing apparatus"></div>
    </section>

    <section class="offer">
      <h3 class="offer-title">We offer our volunteers:</h3>
      <ul class="offer-list">
        <li>Free professional training</li>
        <li>All equipment supplied</li>
        <li>Tax abatements for active volunteers</li>
      </ul>
    </section>

    <p class="more-info">For more information, you can check us out at:
      <span class="web">BrookmereCrestFire.example</span>
    </p>

    <footer class="footer-band">
      <span>37 Quarry Bend Lane</span>
      <span class="sep"></span>
      <span>Drill every Tuesday at 7pm</span>
    </footer>
  </main>
</body>
</html>
```